Lanternfield Advisory logo/business card design -- a digital consulting company

I've just restarted a consulting company I had years ago--Lanternfield Advisory. Now I need a new business card and updated logo. The original logo was simple enough: a chart-like progression atop a grid (see the attached file). I do strategy work, and the chart is meant to show incremental growth and profit. I'd like the reincarnation of my logo to be 3D, with both the grid and arrow rotated on their axis.

I'll want to use the logo on my website as well. I'm open to color schemes, fonts, etc.

Target Market(s)

Business-to-Business. Target market is corporate.

Industry/Entity Type

Business

Contact Information for Business Card

Logo on one-side; name and other contact info on the back

Font styles to use
Serif
Sans Serif

Requirements
Nice to have
• Lanternfield Advisory refers to the concept of "bootstrapping" or making incremental changes to grow with minimal risk and financial exposure, and self-sufficiency (think of the phrase "to pull oneself by one's bootstraps.")

```html
<!DOCTYPE html>
<html lang="en">
<head>
<meta charset="utf-8">
<title>Lanternfield Advisory — Business Card</title>
<link rel="stylesheet" href="https://fonts.googleapis.com/css2?family=Source+Sans+3:wght@400;600;700&display=swap">
<style>
  :root {
    --backdrop: #3b322e;
    --card-white: #f7f6f4;
    --card-black: #1c1c1c;
    --brand-purple: #7a2a7f;
    --ink: #2a2a2a;
    --paper-white: #ffffff;
  }
  html, body {
    margin: 0;
    padding: 0;
    width: 1200px;
    height: 844px;
    overflow: hidden;
    background: var(--backdrop);
    font-family: "Source Sans 3", "Helvetica Neue", Arial, sans-serif;
  }
  .stage {
    position: relative;
    width: 1200px;
    height: 844px;
  }
  .card {
    position: absolute;
    top: 272px;
    width: 525px;
    height: 300px;
    border-radius: 3px;
    box-shadow: 0 10px 24px rgba(0,0,0,0.45);
    box-sizing: border-box;
  }
  .card--contact {
    left: 50px;
    background: var(--card-white);
    color: var(--ink);
  }
  .card--brand {
    left: 625px;
    background: var(--card-black);
    color: var(--paper-white);
    display: flex;
    align-items: center;
    justify-content: center;
  }

  /* brand lockup */
  .brand {
    display: flex;
    align-items: center;
    gap: 10px;
    font-weight: 700;
    letter-spacing: 0.01em;
    line-height: 1;
  }
  .brand__mark {
    width: 14px;
    height: 14px;
    border-radius: 50%;
    background: currentColor;
    flex: none;
  }
  .card--contact .brand {
    position: absolute;
    top: 48px;
    right: 36px;
    font-size: 27px;
    color: var(--brand-purple);
  }
  .card--brand .brand {
    font-size: 40px;
    color: var(--paper-white);
  }
  .card--brand .brand__mark {
    width: 20px;
    height: 20px;
  }

  /* contact details */
  .contact {
    position: absolute;
    left: 36px;
    bottom: 30px;
    font-size: 13.5px;
    line-height: 1.35;
  }
  .contact__name {
    margin: 0;
    font-size: 17px;
    font-weight: 600;
    color: var(--brand-purple);
  }
  .contact__role {
    margin: 0 0 18px;
  }
  .contact__address {
    margin: 0 0 14px;
    font-style: normal;
  }
  .contact__line {
    margin: 0;
  }
  .contact__label {
    color: var(--brand-purple);
    font-weight: 600;
  }
  .contact__label + .contact__value {
    margin-right: 8px;
  }
  .contact__web {
    color: var(--brand-purple);
  }
</style>
</head>
<body>
<main class="stage">
  <section class="card card--contact" aria-label="Business card front">
    <div class="brand">
      <span class="brand__mark" aria-hidden="true"></span>
      <span class="brand__name">Lanternfield Advisory</span>
    </div>

    <div class="contact">
      <p class="contact__name">Daniel Harrow</p>
      <p class="contact__role">Managing Director</p>
      <address class="contact__address">418, Millbrook Lane, Eastvale, 20417</address>
      <p class="contact__line">
        <span class="contact__label">T:</span><span class="contact__value">(021) 408 552 730</span>
        <span class="contact__label">F:</span><span class="contact__value">(021) 408 552 739</span>
        <span class="contact__label">M:</span><span class="contact__value">(021) 408552731</span>
      </p>
      <p class="contact__line">
        <span class="contact__label">E:</span><span class="contact__value">hello@lanternfield.co</span>
        <span class="contact__web">www.lanternfield.co</span>
      </p>
    </div>
  </section>

  <section class="card card--brand" aria-label="Business card back">
    <div class="brand">
      <span class="brand__mark" aria-hidden="true"></span>
      <span class="brand__name">Lanternfield Advisory</span>
    </div>
  </section>
</main>
</body>
</html>
```